Shop window wrapping of a sports betting company

We are a sports betting company in Germany and are looking for a great outside window design for our shops.
Our 3D logo letters look like on the 4 pictures, we have sent you a shop where you can plan your design, what is important here with the shop window foiling is that it should look very modern and exclusive. we also have a website Blauhorn.com where you can take a look.

we have a premium partner a football club Falke Welkau, maybe you can integrate that but of course I'll leave that to you. The partner can be seen on the website.

I have given you a few pictures of how the current outside advertisement and the shop window at one of our locations look like at the moment. Thanks very much

Korun
Updates

Ich brauche zusätzliche Tage um durchzusehen

Target Market(s)

Sports betting

Industry/Entity Type

Ihr dürft das logo auch designen der Name BLAUHORN. Das Trikot format für das TT sollte nicht geändert werden

Requirements
Must have
• Must contain the name blue horn
Nice to have
• we have the best qoutes in all of Germany
Should not have
• Colors shouldn't evade, black red white

```html
<!DOCTYPE html>
<html lang="en">
<head>
<meta charset="utf-8">
<title>Blauhorn – Shop Window Banner</title>
<link rel="stylesheet" href="https://fonts.googleapis.com/css2?family=Oswald:wght@300;500;700&display=swap">
<style>
  :root {
    --stage: #e4e4e4;
    --ink: #0a0a0a;
    --red: #f20000;
    --white: #ffffff;
  }
  html, body {
    margin: 0;
    padding: 0;
    width: 1200px;
    height: 1200px;
    overflow: hidden;
    background: var(--stage);
  }
  .canvas {
    width: 1200px;
    height: 1200px;
    display: flex;
    align-items: center;
    justify-content: center;
  }
  .window-banner {
    width: 1120px;
    height: 449px;
    display: block;
    box-shadow: 0 24px 30px -14px rgba(0, 0, 0, 0.45);
  }
  .banner-text {
    font-family: "Oswald", "Arial Narrow", sans-serif;
  }
  .headline-small { font-weight: 500; font-size: 54px; fill: var(--white); }
  .headline-large { font-weight: 700; font-size: 104px; fill: var(--red); }
  .fine-print { font-weight: 300; font-size: 33px; fill: var(--white); }
  .fine-print .accent { fill: var(--red); font-weight: 500; }
  .offer-figure { font-weight: 500; font-size: 170px; fill: var(--white); }
  .offer-figure .percent { fill: var(--red); }
  .offer-label { font-weight: 500; font-size: 58px; fill: var(--white); }
  .offer-label .accent { fill: var(--red); }
  .ampersand { font-weight: 700; font-size: 96px; fill: var(--white); }
  .brand-name { font-weight: 700; font-size: 100px; fill: var(--white); }
</style>
</head>
<body>
<main class="canvas">
  <svg class="window-banner" viewBox="0 0 1645 660" xmlns="http://www.w3.org/2000/svg" aria-label="Blauhorn shop window banner">
    <defs>
      <linearGradient id="panel-light" x1="0" y1="0" x2="1" y2="1">
        <stop offset="0" stop-color="#dcdcdc"/>
        <stop offset="0.6" stop-color="#f4f4f4"/>
        <stop offset="1" stop-color="#ffffff"/>
      </linearGradient>
      <linearGradient id="athletes-tone" x1="0" y1="0" x2="1" y2="0">
        <stop offset="0" stop-color="#9a9a9a"/>
        <stop offset="0.7" stop-color="#cfcfcf"/>
        <stop offset="1" stop-color="#e6e6e6" stop-opacity="0"/>
      </linearGradient>
      <linearGradient id="fans-tone" x1="0" y1="0" x2="1" y2="1">
        <stop offset="0" stop-color="#2a2a2a"/>
        <stop offset="0.5" stop-color="#4a4a4a"/>
        <stop offset="1" stop-color="#222222"/>
      </linearGradient>
    </defs>

    <rect class="panel-base" x="0" y="0" width="1645" height="660" fill="url(#panel-light)"/>

    <rect class="photo-athletes" x="0" y="30" width="510" height="630" fill="url(#athletes-tone)"
          role="img" aria-label="Black and white photo of a footballer striking a ball and an American football player running"/>

    <polygon class="band-black" points="685,182 1139,182 730,660 272,660" fill="var(--ink)"/>

    <polygon class="band-red" points="1167,182 1267,182 857,660 757,660" fill="var(--red)"/>

    <polygon class="photo-fans" points="1457,0 1645,0 1645,660 882,660"
             fill="url(#fans-tone)"
             role="img" aria-label="Black and white photo of cheering sports fans"/>

    <rect class="brand-plate" x="554" y="27" width="710" height="128" fill="var(--ink)"/>
    <text class="banner-text brand-name" x="627" y="126" textLength="553" lengthAdjust="spacingAndGlyphs">BLAUHORN</text>

    <text class="banner-text headline-small" x="652" y="292" textLength="305" lengthAdjust="spacingAndGlyphs">WIN WITH THE</text>
    <text class="banner-text headline-large" x="625" y="384" textLength="335" lengthAdjust="spacingAndGlyphs">KING OF</text>
    <text class="banner-text headline-large" x="622" y="472" textLength="223" lengthAdjust="spacingAndGlyphs">ODDS</text>

    <text class="banner-text fine-print" x="438" y="576" textLength="292" lengthAdjust="spacingAndGlyphs">CASHBACK IS CREDITED</text>
    <text class="banner-text fine-print" x="395" y="616" textLength="335" lengthAdjust="spacingAndGlyphs"><tspan class="accent">21ST</tspan> DAY OF EVERY <tspan class="accent">MONTH</tspan></text>

    <text class="banner-text offer-figure" x="1384" y="272" textLength="213" lengthAdjust="spacingAndGlyphs">0<tspan class="percent">%</tspan></text>
    <text class="banner-text offer-label" x="1300" y="338" textLength="297" lengthAdjust="spacingAndGlyphs">BETTING FEES</text>
    <text class="banner-text ampersand" x="1197" y="428">&amp;</text>
    <text class="banner-text offer-figure" x="1300" y="535" textLength="297" lengthAdjust="spacingAndGlyphs">20<tspan class="percent">%</tspan></text>
    <text class="banner-text offer-label" x="1304" y="612" textLength="290" lengthAdjust="spacingAndGlyphs">CA<tspan class="accent">$</tspan>HBACK</text>
  </svg>
</main>
</body>
</html>
```